New Business Card Design for Manufacturing

We are an engineering/manufacturing company that offers Advanced machining/assembly/engineering services, as well as innovative products for the heavy duty engine cooling markets.

We are looking to get a new business card designed that is clean and modern looking, but still fits the wide range of technical/skilled work we do.

- We hope to use this design as the base for other design work in new Presentations, web, and print work.

Industry/Entity Type

Engineering

Contact Information for Business Card

Our preferred color of blue is (RGB) 22/71/159 but can vary slightly from that color. Our content will be our Logo and full company name (Fabricated Tooling Works, Inc.), company address, name, job title, phone number with extension, cell number, fax number, website, and email address on the cards.
We'd like the full company name next to the logo, but we are open to other interpretations of that layout.
Preferably, we would like the back side to be clean with just our logo, and the front to contain all of the contact information.

Colors
2f74b4
0355a3
85abd2

Requirements
Must have
• - Logo, company name, needed content - We are open to interpretation beyond that.
• - Standard size business card.
• - Horizontal orientation.
• - Enough space for lengthy names / job titles (for example, a job title could read "Directory of Human Resources" or "V.P. of Governmental Affairs"). We need this to look clean, whether the title be short (CEO) or long (as described above).

```html
<!DOCTYPE html>
<html lang="en">
<head>
<meta charset="utf-8">
<title>Fabricated Tooling Works – Business Card</title>
<link href="https://fonts.googleapis.com/css2?family=Montserrat:wght@400;700;800&family=Questrial&family=Roboto+Condensed:wght@400;700&display=swap" rel="stylesheet">
<style>
  :root {
    --brand-blue: #17479f;
    --accent-blue: #2f74b4;
    --light-blue: #85abd2;
    --charcoal: #3a3a3c;
    --white: #ffffff;
    --ink: #4a4a4c;
    --backdrop: #d9d9d9;
  }
  * { margin: 0; padding: 0; box-sizing: border-box; }
  html, body { width: 1200px; height: 720px; overflow: hidden; }
  body {
    background: var(--backdrop);
    position: relative;
    font-family: "Montserrat", sans-serif;
  }
  .card {
    position: absolute;
    top: 210px;
    width: 525px;
    height: 300px;
    overflow: hidden;
  }
  .card-front { left: 55px; }
  .card-back { left: 620px; background: var(--brand-blue); }
  .card-shapes { position: absolute; inset: 0; }

  .company-name {
    position: absolute; left: 26px; top: 70px;
    color: var(--white);
    font-weight: 800; font-size: 15px; line-height: 15px;
    letter-spacing: 0.3px; text-transform: uppercase;
  }
  .company-name .suffix { font-size: 7px; vertical-align: top; margin-left: 2px; }
  .website {
    position: absolute; left: 26px; top: 130px;
    display: flex; align-items: center; gap: 7px;
    color: var(--white); font-size: 11px;
  }
  .hq {
    position: absolute; left: 26px; top: 200px;
    color: var(--white);
    font-family: "Roboto Condensed", sans-serif;
    font-size: 10.5px; line-height: 13px;
  }
  .hq-title { font-weight: 700; font-size: 13.5px; margin-bottom: 3px; }

  .brand-mark {
    position: absolute;
    display: flex; align-items: center; gap: 8px;
    font-weight: 800; letter-spacing: 1px;
  }
  .card-front .brand-mark { left: 318px; top: 42px; color: var(--white); font-size: 46px; }
  .brand-square { width: 14px; height: 14px; background: currentColor; }

  .person {
    position: absolute; left: 354px; top: 176px;
    color: var(--ink);
    font-family: "Questrial", sans-serif;
    white-space: nowrap;
  }
  .person-name { font-size: 18px; line-height: 22px; letter-spacing: 0.2px; text-transform: uppercase; }
  .person-title {
    font-size: 8.5px; letter-spacing: 0.4px; text-transform: uppercase;
    border-bottom: 1px solid var(--ink); padding-bottom: 2px; margin-top: 2px;
    display: inline-block;
  }

  .back-band {
    position: absolute; left: 0; right: 0; top: 78px; height: 144px;
    background: var(--white);
  }
  .card-back .brand-mark {
    left: 0; right: 0; top: 118px; justify-content: center;
    color: var(--brand-blue); font-size: 52px;
  }
</style>
</head>
<body>

<section class="card card-front" aria-label="Business card front">
  <svg class="card-shapes" width="525" height="300" viewBox="0 0 525 300" aria-hidden="true">
    <rect width="525" height="300" fill="var(--charcoal)"/>
    <polygon points="300,150 525,150 525,252 340,252" fill="var(--white)"/>
    <polygon points="262,150 300,150 345,268 306,268" fill="var(--accent-blue)"/>
    <polygon points="0,0 268,0 254,190 346,300 0,300" fill="var(--brand-blue)"/>
    <polyline points="276,0 262,190 354,300" fill="none" stroke="var(--accent-blue)" stroke-width="4"/>
    <rect x="0" y="160" width="180" height="7" fill="var(--white)"/>
  </svg>

  <div class="company-name">Fabricated<br>Tooling<br>Works<span class="suffix">Inc</span></div>

  <div class="website">
    <svg width="14" height="14" viewBox="0 0 14 14" aria-hidden="true">
      <g fill="none" stroke="var(--white)" stroke-width="1.1">
        <circle cx="7" cy="7" r="6"/>
        <ellipse cx="7" cy="7" rx="2.6" ry="6"/>
        <line x1="1" y1="7" x2="13" y2="7"/>
      </g>
    </svg>
    <span>www.ftw-tooling.com</span>
  </div>

  <div class="hq">
    <div class="hq-title">Corporate Headquarters</div>
    <div>4120 W. Harbor Road, Marquette,</div>
    <div>Michigan 49855</div>
    <div>Phone: (555) 214-3307</div>
    <div>Fax: (555) 214-3390</div>
  </div>

  <div class="brand-mark"><span class="brand-square"></span>FTW</div>

  <div class="person">
    <div class="person-name">Daniel Morrow</div>
    <div class="person-title">Chairman, President &amp; CEO</div>
  </div>
</section>

<section class="card card-back" aria-label="Business card back">
  <div class="back-band"></div>
  <div class="brand-mark"><span class="brand-square"></span>FTW</div>
</section>

</body>
</html>
```